Sticker label for natural moisturizer

I need a sticker label designed for a homemade moisturizer made from beef tallow and honey.
Must include: Logo, product name (Classic Suet & Clover Balm), ingredients (in English and Polish, can use placeholder text for initial design), brief description of product with instructions for use (in English and Polish, can use placeholder text for initial design), manufacturer name (vorelmart.com), manufacturer address (placeholder text for initial design), volume of container (60ml / 2oz)
The product is used by both males and females of all ages, so must be unisex design with broad appeal.
Dimensions: Length 15cm, Height 3cm
Style: Has to simultaneously communicate that this is a homemade product with no chemical fillers AND that it is of extremely high quality.
Brand colors:
#57665C
#FCFAF6
#FFFFFF
#000000
#B99B83
#EAE4DD
#CC8E5A

```html
<!DOCTYPE html>
<html lang="en">
<head>
<meta charset="utf-8">
<title>morra – Classic Suet &amp; Clover Balm label</title>
<link href="https://fonts.googleapis.com/css2?family=M+PLUS+Rounded+1c:wght@400;700&family=Bitter:wght@700&display=swap" rel="stylesheet">
<style>
  :root {
    --sage: #57665C;
    --cream: #FCFAF6;
    --white: #FFFFFF;
    --sand: #EAE4DD;
    --copper: #CC8E5A;
    --taupe: #B99B83;
    --page: #FFFFFF;
  }
  * { box-sizing: border-box; margin: 0; padding: 0; }
  html, body {
    width: 1200px; height: 544px; overflow: hidden;
    background: var(--page);
    font-family: "M PLUS Rounded 1c", "Helvetica Neue", Arial, sans-serif;
  }
  .canvas { position: relative; width: 1200px; height: 544px; }

  .label {
    position: absolute; left: 50px; top: 66px;
    width: 1100px; height: 220px;
    background: var(--white);
  }
  .band-top {
    position: absolute; left: 0; top: 0; width: 100%; height: 102px;
    background: var(--sage); color: var(--cream);
  }
  .band-bottom {
    position: absolute; left: 0; top: 107px; width: 100%; height: 113px;
    background: var(--copper); color: var(--cream);
  }

  .ingredients {
    position: absolute; left: 27px; top: 13px; width: 262px;
    font-size: 10.4px; line-height: 13.4px; letter-spacing: 0.1px;
  }
  .ingredients strong, .instructions strong, .address strong {
    font-weight: 700; font-size: 11.4px; letter-spacing: 0.2px;
  }
  .brand-name {
    position: absolute; left: 549px; top: 48px;
    transform: translate(-50%, -50%);
    font-size: 84px; font-weight: 700; line-height: 1; letter-spacing: -1px;
    color: var(--sand);
  }
  .instructions {
    position: absolute; left: 826px; top: 13px; width: 250px;
    font-size: 10.4px; line-height: 13.4px; letter-spacing: 0.1px;
  }

  .badges { position: absolute; left: 40px; top: 34px; height: 52px; }
  .badge { position: absolute; top: 0; }

  .product-art {
    position: absolute; left: 363px; top: 6px; width: 124px; height: 72px;
  }
  .product-name {
    position: absolute; right: 364px; top: 8px;
    font-family: "Bitter", "Roboto Slab", Georgia, serif; font-weight: 700;
    font-size: 29px; line-height: 30px; text-align: right;
    color: var(--sage); letter-spacing: 0.2px;
  }
  .volume {
    position: absolute; left: 507px; top: 82px; width: 89px; height: 22px;
    background: var(--white); color: var(--copper);
    font-size: 14px; line-height: 22px; text-align: center;
  }
  .address {
    position: absolute; left: 826px; top: 13px; width: 250px;
    font-size: 10.4px; line-height: 13.4px; letter-spacing: 0.1px;
  }
  .website {
    position: absolute; left: 949px; top: 77px; transform: translateX(-50%);
    font-size: 17px; letter-spacing: 0.5px;
  }
</style>
</head>
<body>
<div class="canvas">
  <div class="label">
    <section class="band-top">
      <p class="ingredients"><strong>Ingredients / Składniki:</strong> 100% Grass-fed Irish Beef Tallow (Tallow), Cold Pressed Extra-virgin Olive Oil (Olea Europaea Fruit Oil), Beeswax (Cera Alba), Raw Irish Honey (Mel), Essential oils of Frankincense Carterii (Boswellia carterii), Neroli (Citrus aurantium amara)</p>
      <h1 class="brand-name">morra</h1>
      <p class="instructions"><strong>Instructions / Sposób użycia:</strong><br>Lorem ipsum dolor sit amet, consectetuer adipiscing elit, sed diam nonummy nibh euismod tincidunt ut laoreet dolore magna aliquam erat volutpat. Ut wisi enim ad minim veniam, quis nostrud exerci tation</p>
    </section>

    <section class="band-bottom">
      <div class="badges">
        <svg class="badge" style="left:0" width="38" height="51" viewBox="0 0 38 51" role="img" aria-label="Natural ingredients badge">
          <rect x="1" y="1" width="36" height="49" rx="5" fill="none" stroke="#FFFFFF" stroke-width="2"/>
          <rect x="5" y="5" width="28" height="41" rx="3" fill="#FFFFFF"/>
        </svg>
        <svg class="badge" style="left:49px" width="38" height="51" viewBox="0 0 38 51" role="img" aria-label="No chemicals badge">
          <rect x="1" y="1" width="36" height="49" rx="5" fill="none" stroke="#FFFFFF" stroke-width="2"/>
          <rect x="5" y="5" width="28" height="41" rx="3" fill="#FFFFFF"/>
        </svg>
        <svg class="badge" style="left:95px" width="48" height="50" viewBox="0 0 48 50" role="img" aria-label="BPA free badge">
          <circle cx="24" cy="26" r="23" fill="#FFFFFF"/>
        </svg>
        <svg class="badge" style="left:151px" width="56" height="50" viewBox="0 0 56 50" role="img" aria-label="Homemade badge">
          <circle cx="28" cy="25" r="24" fill="none" stroke="#FFFFFF" stroke-width="2"/>
          <circle cx="28" cy="25" r="18" fill="none" stroke="#FFFFFF" stroke-width="1.5"/>
        </svg>
      </div>

      <div class="product-art" role="img" aria-label="Sketch of a honey pot, bowl of balm and honeycomb"
           style="background: radial-gradient(ellipse at 50% 55%, rgba(87,102,92,0.35), rgba(87,102,92,0.12) 60%, rgba(87,102,92,0) 75%);"></div>
      <h2 class="product-name">Classic Suet &amp;<br>Clover Balm</h2>
      <p class="volume">60ml / 2oz</p>

      <p class="address"><strong>Manufacturer address</strong><br>Lorem ipsum dolor sit amet, consectetuer adipiscing elit, sed diam nonummy nibh</p>
      <p class="website">vorelmart.com</p>
    </section>
  </div>
</div>
</body>
</html>
```